Fernvale Modern Health Food - Takeaway Menu Design

We are looking for a fresh new takeaway menu that signifies our values: Happy, Healthy, Whole. Fernvale is a modern health food restaurant focusing on locally sourced ingredients where everything is made fresh in house. Menu design will display our menu items and food costs. Will provide logo and list of menu items...
Many items, color pallete, and design ideas can be found on our menu section at www.bimlafernvale.ca
Target Market(s)
Customers and possible catering targets...
Industry/Entity Type
Restaurant
Requirements
Must have
- Logo, menu items with pricing, 2 or 3 fold takeaway design, address, website, phone number

```html
<!DOCTYPE html>
<html lang="en">
<head>
<meta charset="utf-8">
<title>Fernvale Modern Health Food – Takeaway Menu</title>
<link href="https://fonts.googleapis.com/css2?family=Kaushan+Script&family=Cutive&display=swap" rel="stylesheet">
<style>
  :root{
    --bg:#ececec;
    --paper:#ffffff;
    --teal:#37a7a6;
    --teal-wash:#c8e7e8;
    --sand-wash:#ddd6cc;
    --ink:#262626;
    --ink-soft:#4a4a4a;
    --stitch:#8b7556;
    --line-art:rgba(255,255,255,.4);
  }
  *{box-sizing:border-box;margin:0;padding:0}
  html,body{width:1200px;height:1200px;overflow:hidden;background:var(--bg)}
  .spread-holder{position:absolute;left:30px;top:190px;width:1149px;height:812px}
  .spread{position:absolute;left:0;top:0;width:1436px;height:1015px;transform:scale(.8);transform-origin:0 0;
    background:var(--paper);box-shadow:0 2px 6px rgba(0,0,0,.18);font-family:"Cutive",serif;color:var(--ink);overflow:hidden}
  .washes{position:absolute;inset:0}
  .fold{position:absolute;left:716px;top:0;width:4px;height:100%;background:linear-gradient(90deg,rgba(0,0,0,.08),rgba(0,0,0,0))}
  .frame{position:absolute;top:8px;height:999px;border:2px dashed var(--stitch)}
  .frame--left{left:8px;width:702px}
  .frame--right{left:727px;width:701px}
  .art{position:absolute;background:var(--line-art);border-radius:40px}
  .heading{position:absolute;font-family:"Kaushan Script",cursive;color:var(--teal);font-weight:400;font-size:42px;line-height:1;white-space:nowrap}
  .note{position:absolute;font-size:12px;line-height:13px;color:var(--ink);white-space:nowrap}
  .note--rule{border-bottom:1px dotted var(--ink-soft);padding-bottom:1px}
  .col{position:absolute}
  .item{margin-bottom:7px}
  .item__row{display:flex;align-items:baseline;font-size:14.5px;line-height:17px;white-space:nowrap;letter-spacing:-.2px}
  .item__name{flex:none}
  .item__price{flex:none}
  .item__dots{flex:1;border-bottom:2px dotted var(--ink);margin:0 2px 4px;min-width:4px}
  .item__desc{font-size:10px;line-height:10.6px;color:var(--ink-soft)}
  .center{position:absolute;text-align:center;font-size:14px;line-height:15px}
</style>
</head>
<body>
<div class="spread-holder">
<main class="spread">
  <svg class="washes" width="1436" height="1015" viewBox="0 0 1436 1015" aria-hidden="true">
    <path fill="var(--sand-wash)" d="M0 0H375C400 60 382 150 405 210C435 270 480 295 530 300C610 305 680 306 716 300V392C600 388 300 396 0 405Z"/>
    <path fill="var(--sand-wash)" d="M1050 0H1436V395C1350 402 1250 382 1180 352C1100 315 1040 205 1048 120C1052 60 1035 20 1050 0Z"/>
    <path fill="var(--teal-wash)" d="M40 610C150 555 350 590 450 520C520 470 650 480 760 498C900 515 1040 540 1150 565C1250 605 1300 700 1290 800C1280 900 1210 975 1120 1015H70C25 900 20 700 40 610Z"/>
  </svg>
  <div class="fold"></div>
  <div class="frame frame--left"></div>
  <div class="frame frame--right"></div>

  <div class="art" role="img" aria-label="White line drawing of a carrot" style="left:10px;top:10px;width:80px;height:345px"></div>
  <div class="art" role="img" aria-label="White line drawing of peas in a pod" style="left:1110px;top:12px;width:318px;height:250px"></div>
  <div class="art" role="img" aria-label="White line drawing of a bell pepper" style="left:680px;top:525px;width:310px;height:320px"></div>
  <div class="art" role="img" aria-label="White line drawing of an artichoke" style="left:515px;top:860px;width:150px;height:150px"></div>
  <div class="art" role="img" aria-label="White line drawing of a watermelon slice and strawberry" style="left:775px;top:815px;width:290px;height:195px"></div>

  <!-- Rice Bowls -->
  <h2 class="heading" style="left:293px;top:40px">Rice Bowls</h2>
  <p class="note note--rule" style="left:294px;top:96px">For the following menu items:<br>add Chicken $3.00 / add Tofu $2.50</p>
  <div class="col" style="left:98px;top:144px;width:255px">
    <div class="item"><div class="item__row"><span class="item__name">Coconut Chili Bowl</span><span class="item__dots"></span><span class="item__price">$12.25</span></div><p class="item__desc">Brown Rice, kidney beans, chickpeas, corn, red onion, coconut milk, greens, grated carrot, Fernvale chili spice blend</p></div>
    <div class="item"><div class="item__row"><span class="item__name">Falafel Bowl</span><span class="item__dots"></span><span class="item__price">$12.25</span></div><p class="item__desc">Brown rice, gf falafels, greens, hummus, banana peppers, red onion, cucumber, house cilantro lime sc</p></div>
    <div class="item"><div class="item__row"><span class="item__name">Urban Bowl</span><span class="item__dots"></span><span class="item__price">$12.25</span></div><p class="item__desc">Brown rice, greens, grated carrot, beets, red cabbage, tamari mushrooms, hemp hearts, sprouts, house tamari sc</p></div>
  </div>
  <div class="col" style="left:385px;top:144px;width:254px">
    <div class="item"><div class="item__row"><span class="item__name">Miso BBQ Bowl</span><span class="item__dots"></span><span class="item__price">$12.25</span></div><p class="item__desc">Brown rice, greens, bbq tempeh, sweet potato, grated carrot, beet, pickled onion, pumpkin seeds, house bbq miso sc</p></div>
    <div class="item"><div class="item__row"><span class="item__name">Red Curry Bowl</span><span class="item__dots"></span><span class="item__price">$12.25</span></div><p class="item__desc">Brown rice, greens, avocado, black beans, carrot, cucumber, salsa, yogurt, house red curry sc</p></div>
  </div>

  <!-- Grilled Sandwiches -->
  <h2 class="heading" style="left:350px;top:310px">Grilled Sandwiches</h2>
  <p class="note note--rule" style="left:478px;top:366px">Sprouted grain or Gluten free</p>
  <div class="col" style="left:61px;top:396px;width:296px">
    <div class="item"><div class="item__row"><span class="item__name">Grilled Breakfast Sandwich</span><span class="item__dots"></span><span class="item__price">$9.95</span></div><p class="item__desc">Fried egg on hillcrest micro sour bread, with smoked gouda, tomato, and spinach, served with a side of russian sauce. (Add montreal smoked beef or turkey bacon $3.00)</p></div>
    <div class="item"><div class="item__row"><span class="item__name">Spicy Chicken</span><span class="item__dots"></span><span class="item__price">$9.95</span></div><p class="item__desc">Chicken breast, smoked gouda, spinach, tomato, banana peppers, chipotle mayo</p></div>
    <div class="item"><div class="item__row"><span class="item__name">Fernvale Reuben</span><span class="item__dots"></span><span class="item__price">$9.95</span></div><p class="item__desc">Montreal smoked beef, saurkraut, smoked gouda, dijon mustard, house russian sc</p></div>
  </div>
  <div class="col" style="left:387px;top:396px;width:276px">
    <div class="item"><div class="item__row"><span class="item__name">Carrot Tempeh</span><span class="item__dots"></span><span class="item__price">$9.95</span></div><p class="item__desc">Smoked bbq temph, grated carrot, greens, tomato, avocado, red onion, dijon mustard, bbq miso sauce</p></div>
    <div class="item"><div class="item__row"><span class="item__name">Black Bean Torta</span><span class="item__dots"></span><span class="item__price">$9.95</span></div><p class="item__desc">Creamy black beans, greens, tomatoes, pickled red onion, avocado, chipotle mayo</p></div>
    <div class="item"><div class="item__row"><span class="item__name">Lentil Veggie Burger</span><span class="item__dots"></span><span class="item__price">$9.95</span></div><p class="item__desc">Lentil &amp; sweet potato pattie, tomato avocado, soy cheese, dijon mustard, served on a spelt bun, house chipotle mayo</p></div>
  </div>

  <!-- Grilled Wraps -->
  <h2 class="heading" style="left:93px;top:600px">Grilled Wraps</h2>
  <p class="note note--rule" style="left:111px;top:653px">Sprouted grain or Gluten free</p>
  <div class="col" style="left:76px;top:684px;width:274px">
    <div class="item"><div class="item__row"><span class="item__name">Breakfast Burrito</span><span class="item__dots"></span><span class="item__price">$10.95</span></div><p class="item__desc">Your choice of egg or tofu scramble, avocado, tomato, gouda, salsa, spinach, served with a side of salsa</p></div>
    <div class="item"><div class="item__row"><span class="item__name">Falafel</span><span class="item__dots"></span><span class="item__price">$10.95</span></div><p class="item__desc">Brown rice, baked falafels, hummus, avocado, red cabbage, pickled onion, spinach, house cilantro lime sc</p></div>
    <div class="item"><div class="item__row"><span class="item__name">Veggie Burrito</span><span class="item__dots"></span><span class="item__price">$10.95</span></div><p class="item__desc">Brown rice, black beans, corn, sweet potato, red cabbage, house coconut chipotle mayo</p></div>
    <div class="item"><div class="item__row"><span class="item__name">BBQ Chicken</span><span class="item__dots"></span><span class="item__price">$10.95</span></div><p class="item__desc">Chicken, brown rice, organic greens, red cabbage, avocado, bbq miso sauce</p></div>
    <div class="item"><div class="item__row"><span class="item__name">Urban Wrap</span><span class="item__dots"></span><span class="item__price">$10.95</span></div><p class="item__desc">Brown rice, organic greens, grated carrots, beets, purple cabbage, tamari</p></div>
  </div>

  <!-- Daily Salad & Soup -->
  <h2 class="heading" style="left:410px;top:605px;width:240px;text-align:center">Daily Salad</h2>
  <p class="center" style="left:410px;top:670px;width:240px">Your choice of salads,<br>$4.95 side $3.75</p>
  <h2 class="heading" style="left:410px;top:735px;width:240px;text-align:center">Daily Soup</h2>
  <p class="center" style="left:385px;top:800px;width:290px">Farm to Table, fresh and inspired<br>$6.00 side $4.00</p>

  <!-- Fernvale Breakfast -->
  <h2 class="heading" style="left:758px;top:85px">Fernvale Breakfast</h2>
  <p class="note note--rule" style="left:758px;top:136px">- add Serving local farm fresh eggs<br>- add Served until 12pm weekdays &amp; 2pm weekends</p>
  <div class="col" style="left:756px;top:181px;width:307px">
    <div class="item"><div class="item__row"><span class="item__name">Breakfast Bowl</span><span class="item__dots"></span><span class="item__price">$12.00</span></div><p class="item__desc">Roasted roots topped with two poached eggs, black beans, rice, avocado, banana peppers spinach and salsa topped with our house made cilantro lime dressing</p></div>
    <div class="item"><div class="item__row"><span class="item__name">Pancakes</span><span class="item__dots"></span><span class="item__price">$8.95</span></div><p class="item__desc">3 buckwheat pancakes, turkey bacon, or montreal smoked beef w/ maple syrup or, side of fruit or roots</p></div>
    <div class="item"><div class="item__row"><span class="item__name">Grilled Breakfast Burrito</span><span class="item__dots"></span><span class="item__price">$10.95</span></div><p class="item__desc">Your choice of egg or tofu scramble, avocado, tomato, gouda, salsa, spinach, served with a side of salsa</p></div>
    <div class="item"><div class="item__row"><span class="item__name">Two Eggs (your way)</span><span class="item__dots"></span><span class="item__price">$8.95</span></div><p class="item__desc">Eggs, toast, turkey bacon or corned beef and roasted roots</p></div>
    <div class="item"><div class="item__row"><span class="item__name">Side Toast</span><span class="item__dots"></span><span class="item__price">$3.95</span></div><p class="item__desc">Two pieces hillcrest micro sour or gluten free bread w/ peanut butter, almond butter or jam</p></div>
    <div class="item"><div class="item__row"><span class="item__name">Side of Pancakes</span><span class="item__dots"></span><span class="item__price">$5.50</span></div><p class="item__desc">Two buckwheat pancakes w/ maple syrup</p></div>
  </div>

  <!-- Eggs Bennie -->
  <div class="col" style="left:1093px;top:312px;width:318px">
    <div class="item__row" style="font-size:16px">Eggs Bennie</div>
    <p class="item__desc">English muffin(available gluten free) two poached eggs, roasted roots, hollandaise served with roasted roots</p>
    <p class="item__desc" style="font-style:italic;text-align:center;font-size:11px;line-height:12px;margin:6px 0 11px">Or have your Bennie in a Bowl served<br>on Roasted Roots!!</p>
    <div class="item"><div class="item__row"><span class="item__name">Very Veggie Bennie</span><span class="item__dots"></span><span class="item__price">$11.95</span></div><p class="item__desc">Spinach, tomato, avocado</p></div>
    <div class="item"><div class="item__row"><span class="item__name">Montreal Smoked Beef Bennie</span><span class="item__dots"></span><span class="item__price">$12.25</span></div><p class="item__desc">Montreal smoked beef, spinach, tomato</p></div>
    <div class="item"><div class="item__row"><span class="item__name">Smoked Salmon Bennie</span><span class="item__dots"></span><span class="item__price">$13.95</span></div><p class="item__desc">Smoked salmon, spinach, capers</p></div>
  </div>

  <!-- Smoothies -->
  <h2 class="heading" style="left:1190px;top:548px">Smoothies</h2>
  <p class="note" style="left:1303px;top:594px;font-size:19px;line-height:21px">16oz</p>
  <div class="col" style="left:1088px;top:638px;width:277px">
    <div class="item"><div class="item__row"><span class="item__name">Mylkshake</span><span class="item__dots"></span><span class="item__price">$6.75</span></div><p class="item__desc">Almond milk, avocado, banana, vanilla, matcha, dates</p></div>
    <div class="item"><div class="item__row"><span class="item__name">Breakfast Smoothie</span><span class="item__dots"></span><span class="item__price">$6.75</span></div><p class="item__desc">Mixed berries, banana, spinach, almond milk &amp; coconut water</p></div>
    <div class="item"><div class="item__row"><span class="item__name">Green Protein</span><span class="item__dots"></span><span class="item__price">$7.25</span></div><p class="item__desc">Kale, spinach, lemon, almond meal, avocado, spirulina, honey, vanilla, banana, dates, almond milk</p></div>
    <div class="item"><div class="item__row"><span class="item__name">Frozen Hot Chocolate</span><span class="item__dots"></span><span class="item__price">$6.75</span></div><p class="item__desc">Cacao, macca, dates, cinnamon, avocado, honey, vanilla coconut milk</p></div>
    <div class="item"><div class="item__row"><span class="item__name">Brain Booster</span><span class="item__dots"></span><span class="item__price">$6.75</span></div><p class="item__desc">Carrot juice, blueberries, beet, apple, ginger, lemon, almond milk</p></div>
    <div class="item"><div class="item__row"><span class="item__name">Blueberry Matcha</span><span class="item__dots"></span><span class="item__price">$6.75</span></div><p class="item__desc">Blueberries, banana, dates, matcha, cinnamon, almond milk</p></div>
  </div>
</main>
</div>
</body>
</html>
```